Invitation Design Project

50th Birthday Party for Tim. Big, loud party planned with loads of friends and family. at our home. Decorations will be coloured lanterns attached to the pergola and hired a band.

Details:

on 19th October, 2013
(other details when design chosen)
at: 7.00 pm
RSVP: 14th October, 2013

```html
<!DOCTYPE html>
<html lang="en">
<head>
<meta charset="utf-8">
<title>Fifty + Fabulous – Tim's 50th Birthday Invitation</title>
<link rel="stylesheet" href="https://fonts.googleapis.com/css2?family=Great+Vibes&family=Montserrat:wght@300;400;600&display=swap">
<style>
  :root {
    --backdrop: #2e2a27;
    --ink-white: #ffffff;
    --accent-pink: #f08a8a;
    --tone-gold: #e2ad3e;
    --tone-orange: #e8863a;
    --tone-coral: #e4683f;
    --tone-red: #d9553c;
    --tone-teal: #4f8a78;
  }
  * { margin: 0; padding: 0; box-sizing: border-box; }
  html, body {
    width: 1200px;
    height: 1000px;
    overflow: hidden;
    background: var(--backdrop);
  }
  .invitation {
    position: absolute;
    left: 315px;
    top: 95px;
    width: 570px;
    height: 810px;
    overflow: hidden;
    color: var(--ink-white);
  }
  .invitation__pattern {
    position: absolute;
    inset: 0;
    width: 100%;
    height: 100%;
    display: block;
  }
  .headline {
    position: absolute;
    font-family: "Great Vibes", cursive;
    font-weight: 400;
    line-height: 1;
    color: var(--ink-white);
    white-space: nowrap;
  }
  .headline--fifty { left: 4px; top: 42px; font-size: 150px; }
  .headline--amp { left: 365px; top: 58px; font-size: 56px; }
  .headline--plus {
    left: 106px; top: 218px;
    font-family: "Montserrat", sans-serif;
    font-weight: 300;
    font-size: 40px;
    color: var(--accent-pink);
  }
  .headline--fabulous { left: 22px; top: 218px; font-size: 158px; }
  .details {
    position: absolute;
    left: 268px;
    top: 448px;
    font-family: "Montserrat", sans-serif;
    font-weight: 300;
    white-space: nowrap;
  }
  .details__intro { font-size: 21px; line-height: 29px; letter-spacing: 0.3px; }
  .details__name { font-size: 40px; font-weight: 600; line-height: 46px; margin-top: 8px; }
  .details__event { font-size: 33px; line-height: 38px; }
  .details__when { font-size: 22px; line-height: 30px; margin-top: 6px; }
  .details__rsvp {
    position: absolute;
    left: 268px;
    top: 734px;
    font-family: "Montserrat", sans-serif;
    font-weight: 300;
    font-size: 17px;
  }
</style>
</head>
<body>
  <main class="invitation">
    <svg class="invitation__pattern" viewBox="0 0 570 810" role="img" aria-label="Colourful pattern of overlapping translucent circles and triangles in orange, coral, gold, pink and teal tones">
      <defs>
        <linearGradient id="pattern-tones" x1="0" y1="0" x2="0.35" y2="1">
          <stop offset="0" stop-color="var(--tone-gold)"/>
          <stop offset="0.35" stop-color="var(--tone-coral)"/>
          <stop offset="0.6" stop-color="var(--tone-orange)"/>
          <stop offset="1" stop-color="var(--tone-red)"/>
        </linearGradient>
      </defs>
      <rect width="570" height="810" fill="url(#pattern-tones)"/>
    </svg>

    <h1 class="headline-group">
      <span class="headline headline--fifty">Fifty</span>
      <span class="headline headline--amp">&amp;</span>
      <span class="headline headline--fabulous">Fabulous</span>
      <span class="headline headline--plus">+</span>
    </h1>

    <section class="details">
      <p class="details__intro">Join family and friends<br>as we celebrate the</p>
      <p class="details__name">Tim’s 50th</p>
      <p class="details__event">Birthday Party</p>
      <p class="details__when">19th October, 2013<br>7.00 pm till late</p>
    </section>

    <p class="details__rsvp">RSVP: 14th October, 2013</p>
  </main>
</body>
</html>
```